Mental Health care Company in Washington DC

We are a new mental health care services provider in Washington DC. Please look at these sites.
https://marlowbrookpartners.com
https://www.quillstoneinc.com
https://velmarsh-kt.org/
https://www.trivanqx.com
https://www.thelanternofqz.com

```html
<!DOCTYPE html>
<html lang="en">
<head>
<meta charset="utf-8">
<title>Nuvela Health – Mental Wellness in Washington DC</title>
<link href="https://fonts.googleapis.com/css2?family=Poppins:wght@300;400;500;600;700&family=Montserrat:wght@700;800&family=Caveat:wght@500&display=swap" rel="stylesheet">
<style>
:root{
  --navy:#13264d;
  --navy-2:#1c3563;
  --orange:#f5821f;
  --orange-light:#f9a55a;
  --teal:#5bbfc6;
  --mint:#eef8f7;
  --ink:#1d1d1f;
  --text:#4a4a4a;
  --line:#d9d9d9;
  --white:#ffffff;
}
*{margin:0;padding:0;box-sizing:border-box}
html,body{width:1200px;height:4138px;overflow:hidden}
body{font-family:'Poppins',sans-serif;color:var(--ink);background:var(--white);position:relative}
.abs{position:absolute}
a{color:inherit;text-decoration:none}

/* top bar + header */
.topbar{left:470px;top:0;width:730px;height:29px;background:var(--navy);color:#fff;font-size:10px;display:flex;align-items:center;gap:30px;padding-left:40px}
.topbar::before{content:"";position:absolute;left:-8px;top:0;width:22px;height:29px;background:var(--orange);transform:skewX(35deg)}
.topbar span b{font-weight:500}
.topbar .ico{color:var(--orange);margin-right:5px}
.logo{left:141px;top:22px;display:flex;align-items:center;gap:8px;font-size:30px;font-weight:500;color:var(--navy);letter-spacing:-0.5px}
.logo .dot{width:12px;height:12px;border-radius:50%;background:var(--orange)}
.nav{top:50px;left:0;font-size:13px;color:var(--ink)}
.nav a{position:absolute;white-space:nowrap}
.nav .active{color:var(--orange)}
.btn-contact{left:952px;top:45px;width:106px;height:29px;border-radius:15px;background:var(--orange);color:#fff;font-size:10.5px;font-weight:600;display:flex;align-items:center;justify-content:center}

/* hero */
.hero{left:0;top:88px;width:1200px;height:667px;overflow:hidden;
  background:linear-gradient(90deg,#2b2e33 0%,#3c4045 40%,#6b7075 62%,#b9bec3 80%,#d8dcdf 100%)}
.hero .wave{position:absolute;left:0;top:0}
.hero-kicker{left:141px;top:210px;color:#fff;font-size:22px;font-weight:400}
.hero-title{left:141px;top:244px;color:#fff;font-family:'Montserrat',sans-serif;font-size:44px;line-height:53px;font-weight:800}
.hero-title .teal{color:var(--teal)}
.hero-title .light{font-family:'Poppins',sans-serif;font-weight:400}
.hero-text{left:141px;top:359px;width:410px;color:#fff;font-size:15px;line-height:23px}
.btn-book{left:141px;top:469px;width:199px;height:39px;border-radius:8px;background:var(--orange);color:#fff;font-size:12px;font-weight:600;display:flex;align-items:center;justify-content:center;gap:6px}
.scroll-down{left:570px;top:698px;width:58px;height:58px;border-radius:50%;background:#fff;box-shadow:0 6px 16px rgba(0,0,0,.12);display:flex;align-items:center;justify-content:center}

/* features */
.feature{top:800px;width:300px}
.feature .circle{position:absolute;left:0;top:0;width:62px;height:62px;border-radius:50%;border:1px solid #e5e5e5;display:flex;align-items:center;justify-content:center}
.feature h3{position:absolute;left:84px;top:4px;font-size:14px;font-weight:500;white-space:nowrap}
.feature p{position:absolute;left:84px;top:34px;width:210px;font-size:11px;line-height:19px;color:var(--text)}
.rule{left:103px;top:952px;width:992px;height:1px;background:var(--line)}

/* cta banner */
.cta{left:141px;top:1025px;width:917px;height:208px;border-radius:26px;overflow:hidden;
  background:linear-gradient(90deg,#f5821f 0%,#f7913a 45%,#fbd8b4 62%,#f3f4f6 78%)}
.cta-photo{position:absolute;right:0;top:0;width:330px;height:208px;background:linear-gradient(90deg,rgba(255,255,255,0),#dfe5ea 40%,#c9d3da)}
.cta-script{left:68px;top:38px;font-family:'Caveat',cursive;font-size:25px;color:#ffe3c2}
.cta h2{position:absolute;left:68px;top:68px;width:520px;font-size:22px;line-height:34px;font-weight:500;color:#fff}
.cta-link{left:68px;top:145px;font-size:14px;color:#fff;text-decoration:underline}
.pills{left:1110px;top:1140px;width:90px;height:95px;background:radial-gradient(circle at 60% 40%,#cfe9ef,rgba(255,255,255,0) 70%)}

/* marquee */
.marquee{left:0;top:1320px;width:1200px;height:45px;background:var(--teal);color:#fff;font-size:15px;display:flex;align-items:center;white-space:nowrap;overflow:hidden}
.marquee .track{display:flex;align-items:center;gap:24px;margin-left:-48px}
.marquee .item{display:flex;align-items:center;gap:16px}

/* about */
.about-bg{left:0;top:1368px;width:604px;height:567px;background:var(--mint)}
.about-vline{left:604px;top:1368px;width:1px;height:567px;background:var(--line)}
.about-hline{left:0;top:1935px;width:1200px;height:1px;background:var(--line)}
.about-photo{left:0;top:1453px;width:519px;height:397px;border-radius:0 16px 16px 0;background:linear-gradient(135deg,#4a8fbf 0%,#7fb4d6 45%,#d9e6ee 75%,#b9cad6 100%)}
.eyebrow{font-size:13px;font-weight:500;color:var(--teal);letter-spacing:.3px}
.about-eyebrow{left:673px;top:1460px;display:flex;align-items:center;gap:10px}
.about-eyebrow .dash{width:60px;height:1px;background:var(--line)}
.about h2,.about-title{left:673px;top:1493px;font-size:30px;line-height:36px;font-weight:600;color:var(--navy)}
.about-text{left:673px;top:1578px;width:438px;font-size:12.8px;line-height:22.5px;color:#333}
.btn-orange{border-radius:18px;background:var(--orange);color:#fff;font-size:11.5px;font-weight:600;display:flex;align-items:center;justify-content:center}
.about-btn{left:673px;top:1810px;width:194px;height:36px}

/* services */
.center{left:0;width:1200px;text-align:center}
.svc-eyebrow{top:2024px}
.svc-orn{left:560px;top:2050px;width:80px;height:12px}
.svc-title{top:2066px;font-size:30px;font-weight:500;color:var(--navy)}
.card{top:2142px;width:282px;height:317px;border:1.5px solid #2a2a2a;background:#fff;text-align:center}
.card .img{position:absolute;left:15px;top:15px;width:252px;height:140px}
.card h3{position:absolute;left:0;top:180px;width:100%;font-size:17px;font-weight:500}
.card p{position:absolute;left:20px;top:214px;width:240px;font-size:12px;line-height:23px;color:#444}
.card .badge{position:absolute;left:115px;top:292px;width:52px;height:52px;border-radius:50%;background:var(--teal);border:4px solid #fff;box-shadow:0 0 0 1px #e6f4f5;display:flex;align-items:center;justify-content:center}

/* ready */
.ready{left:0;top:2579px;width:1200px;height:403px;background:var(--orange);overflow:hidden}
.ready-photo{position:absolute;left:0;top:0;width:780px;height:403px;background:linear-gradient(90deg,#cfd5dc 0%,#e7dcd2 40%,#efc9a4 65%,rgba(245,130,31,0) 100%)}
.ready h2{position:absolute;left:630px;top:90px;font-size:35px;line-height:48px;font-weight:600;color:#fff}
.ready p{position:absolute;left:630px;top:203px;width:420px;font-size:13.5px;line-height:24px;color:#fff4e8}
.ready .btn-outline{position:absolute;left:630px;top:276px;width:246px;height:38px;border:1.5px solid #fff;border-radius:20px;color:#fff;font-size:13px;font-weight:500;display:flex;align-items:center;justify-content:center}

/* values strip */
.values{left:-160px;top:3030px;white-space:nowrap;font-size:80px;font-weight:600;line-height:100px;letter-spacing:1px}
.values .outline{color:transparent;-webkit-text-stroke:1.4px #8a8a8a}
.values .solid{color:var(--ink)}

/* testimonials */
.testi-title{top:3180px;font-size:30px;line-height:42px;font-weight:500}
.tcard{top:3330px;width:283px;height:230px;background:#fff;box-shadow:0 4px 22px rgba(0,0,0,.08)}
.tcard .quote{position:absolute;right:0;top:-18px;width:38px;height:38px;border-radius:50%;border:2px solid var(--teal);background:#fff;display:flex;align-items:center;justify-content:center}
.tcard.o .quote{border-color:var(--orange)}
.tcard .avatar{position:absolute;left:20px;top:10px;width:60px;height:60px;border-radius:50%;background:linear-gradient(135deg,#c8ccd1,#7d848c)}
.tcard .stars{position:absolute;left:104px;top:28px;font-size:19px;color:var(--orange);letter-spacing:2px}
.tcard h4{position:absolute;left:22px;top:82px;font-size:13.5px;font-weight:500}
.tcard p{position:absolute;left:22px;top:106px;width:245px;font-size:11.2px;line-height:21px;color:#333}
.dots{left:557px;top:3580px;display:flex;gap:8px}
.dots i{width:11px;height:11px;border-radius:50%;background:#d8d8d8}
.dots i.on{background:var(--orange)}

/* footer */
.footer{left:0;top:3670px;width:1200px;height:468px;background:var(--navy);color:#fff}
.f-logo{left:141px;top:130px;display:flex;align-items:center;gap:8px;font-size:30px;font-weight:500}
.f-logo .dot{width:12px;height:12px;border-radius:50%;background:var(--orange)}
.f-desc{left:138px;top:196px;width:200px;font-size:12px;line-height:21.5px}
.f-head{font-size:16px;font-weight:500;color:var(--orange)}
.f-links{left:368px;top:158px;list-style:none;font-size:12px}
.f-links li{height:32px}
.f-links li::before{content:"•";margin-right:6px}
.f-contact{left:527px;top:158px;width:230px;font-size:12px;line-height:21px}
.f-contact .lbl{color:var(--orange);margin-top:18px}
.f-box{left:781px;top:85px;width:290px;height:254px;border-radius:12px;background:var(--navy-2)}
.f-box .f-head{position:absolute;left:38px;top:30px}
.f-box p{position:absolute;left:38px;top:70px;width:220px;font-size:12px;line-height:21px}
.f-input{position:absolute;left:38px;top:130px;width:218px;height:36px;border-radius:18px;background:#fff;color:#888;font-size:11.5px;display:flex;align-items:center;justify-content:space-between;padding:0 18px 0 20px}
.f-sub{position:absolute;left:38px;top:182px;width:152px;height:36px;border-radius:18px;background:var(--orange);font-size:12.5px;font-weight:500;display:flex;align-items:center;justify-content:space-between;padding:0 18px 0 24px}
.f-rule{left:0;top:409px;width:1200px;height:1px;background:rgba(255,255,255,.18)}
.f-copy{left:141px;top:430px;font-size:12px}
.f-legal{left:756px;top:430px;font-size:12px;display:flex;gap:10px}
</style>
</head>
<body>

<!-- Header -->
<div class="abs topbar">
  <span><span class="ico">&#9990;</span>Call now: <b>(555) 014-2290</b></span>
  <span><span class="ico">&#9993;</span>Email: <b>hello@nuvelahealth.com</b></span>
  <span><span class="ico">&#9719;</span>Time: <b>Mon - Sun, 08:30am to 05:30pm</b></span>
</div>
<div class="abs logo"><span class="dot"></span>Nuvela Health</div>
<nav class="abs nav">
  <a class="active" style="left:511px">Home</a>
  <a style="left:586px">About Us</a>
  <a style="left:681px">Services &#8964;</a>
  <a style="left:784px">Blog</a>
  <a style="left:850px">FAQs</a>
</nav>
<a class="abs btn-contact">Contact Now</a>

<!-- Hero -->
<section class="abs hero" role="img" aria-label="Smiling doctor in a white coat with a stethoscope, standing in a softly lit clinic">
  <svg class="wave" width="1200" height="667" viewBox="0 0 1200 667">
    <path d="M0 538 C250 548 420 650 600 640 C800 628 1000 540 1200 526 L1200 667 L0 667 Z" fill="#fff"/>
  </svg>
  <p class="abs hero-kicker">COMPASSIONATE</p>
  <h1 class="abs hero-title">MENTAL <span class="teal">WELLNESS</span> IN<br><span class="light">WASHINGTON DC</span></h1>
  <p class="abs hero-text">Evidence-based care tailored to your needs. Where clinical expertise meets your unique needs</p>
  <a class="abs btn-book">
    <svg width="14" height="14" viewBox="0 0 14 14"><rect x="1" y="2.5" width="12" height="10.5" rx="1.5" fill="#fff"/><rect x="3" y="0.5" width="2" height="3.5" fill="#fff"/><rect x="9" y="0.5" width="2" height="3.5" fill="#fff"/><rect x="3" y="6" width="8" height="1.2" fill="#f5821f"/></svg>
    BOOK APPOINTMENT</a>
</section>
<div class="abs scroll-down">
  <svg width="22" height="28" viewBox="0 0 22 28"><path d="M11 2 V25 M3 17 L11 25 L19 17" stroke="#f5821f" stroke-width="2" fill="none"/></svg>
</div>

<!-- Features -->
<div class="abs feature" style="left:141px">
  <div class="circle"><svg width="28" height="28" viewBox="0 0 28 28" fill="none" stroke="#f5821f" stroke-width="1.5"><path d="M14 13 C10 9 6 12 9 15 L14 19 L19 15 C22 12 18 9 14 13Z"/><path d="M3 20 H9 L14 23 H22 L25 20"/></svg></div>
  <h3>Personalized Family Care</h3>
  <p>We treat you like family, building lasting relationships based on trust and compassion</p>
</div>
<div class="abs feature" style="left:451px">
  <div class="circle"><svg width="28" height="28" viewBox="0 0 28 28" fill="none" stroke="#5bbfc6" stroke-width="1.5"><path d="M14 4 L23 8 V14 C23 19 19 23 14 25 C9 23 5 19 5 14 V8Z"/><path d="M14 12 C12 10 10 12 11.5 14 L14 16.5 L16.5 14 C18 12 16 10 14 12Z"/></svg></div>
  <h3>Comprehensive Services</h3>
  <p>From routine checkups to specialized testing, we offer a wide range of services to meet your needs</p>
</div>
<div class="abs feature" style="left:769px">
  <div class="circle"><svg width="28" height="28" viewBox="0 0 28 28" fill="none" stroke="#f5821f" stroke-width="1.5"><circle cx="14" cy="12" r="8"/><circle cx="14" cy="12" r="4"/><path d="M10 19 L8 25 L14 22 L20 25 L18 19"/></svg></div>
  <h3>Experienced &amp; Caring Staff</h3>
  <p>Our team of dedicated professionals is committed to providing the highest quality care</p>
</div>
<div class="abs rule"></div>

<!-- CTA banner -->
<section class="abs cta">
  <div class="cta-photo" role="img" aria-label="Doctor in a white coat holding a stethoscope"></div>
  <p class="abs cta-script">Have A Question?</p>
  <h2>Reach out to schedule your appointment or get answers to your questions</h2>
  <a class="abs cta-link">Schedule an Appointment Today!</a>
</section>
<div class="abs pills" role="img" aria-label="Scattered capsules and a medical instrument"></div>

<!-- Marquee -->
<div class="abs marquee">
  <div class="track">
    <span>Private Care</span>
    <span class="item"><svg width="20" height="18" viewBox="0 0 20 18" fill="none" stroke="#fff" stroke-width="1.6"><path d="M10 16 L2.5 8.5 C0 6 1.5 1.5 5.5 1.5 C7.5 1.5 9 3 10 4.5 C11 3 12.5 1.5 14.5 1.5 C18.5 1.5 20 6 17.5 8.5Z"/></svg>Family-Focused</span>
    <span class="item"><svg width="20" height="18" viewBox="0 0 20 18" fill="none" stroke="#fff" stroke-width="1.6"><path d="M10 16 L2.5 8.5 C0 6 1.5 1.5 5.5 1.5 C7.5 1.5 9 3 10 4.5 C11 3 12.5 1.5 14.5 1.5 C18.5 1.5 20 6 17.5 8.5Z"/></svg>Comprehensive Services</span>
    <span class="item"><svg width="20" height="18" viewBox="0 0 20 18" fill="none" stroke="#fff" stroke-width="1.6"><path d="M10 16 L2.5 8.5 C0 6 1.5 1.5 5.5 1.5 C7.5 1.5 9 3 10 4.5 C11 3 12.5 1.5 14.5 1.5 C18.5 1.5 20 6 17.5 8.5Z"/></svg>Advanced Testing</span>
    <span class="item"><svg width="20" height="18" viewBox="0 0 20 18" fill="none" stroke="#fff" stroke-width="1.6"><path d="M10 16 L2.5 8.5 C0 6 1.5 1.5 5.5 1.5 C7.5 1.5 9 3 10 4.5 C11 3 12.5 1.5 14.5 1.5 C18.5 1.5 20 6 17.5 8.5Z"/></svg>Community Health</span>
    <span class="item"><svg width="20" height="18" viewBox="0 0 20 18" fill="none" stroke="#fff" stroke-width="1.6"><path d="M10 16 L2.5 8.5 C0 6 1.5 1.5 5.5 1.5 C7.5 1.5 9 3 10 4.5 C11 3 12.5 1.5 14.5 1.5 C18.5 1.5 20 6 17.5 8.5Z"/></svg>Personalized Healthcare</span>
    <span class="item"><svg width="20" height="18" viewBox="0 0 20 18" fill="none" stroke="#fff" stroke-width="1.6"><path d="M10 16 L2.5 8.5 C0 6 1.5 1.5 5.5 1.5 C7.5 1.5 9 3 10 4.5 C11 3 12.5 1.5 14.5 1.5 C18.5 1.5 20 6 17.5 8.5Z"/></svg>Comprehensive Services</span>
  </div>
</div>

<!-- About -->
<div class="abs about-bg"></div>
<div class="abs about-vline"></div>
<div class="abs about-photo" role="img" aria-label="Father and son high-fiving a smiling nurse in a bright clinic"></div>
<div class="abs about-eyebrow"><span class="eyebrow">WHO WE ARE</span>
  <svg width="16" height="16" viewBox="0 0 16 16"><rect x="6" y="0" width="4" height="6" fill="#f5821f"/><rect x="6" y="10" width="4" height="6" fill="#5bbfc6"/><rect x="0" y="6" width="6" height="4" fill="#5bbfc6"/><rect x="10" y="6" width="6" height="4" fill="#f5821f"/></svg>
  <span class="dash"></span></div>
<h2 class="abs about-title">A Trusted Mental Health<br>Partner In DC</h2>
<p class="abs about-text">Lorem Ipsum is simply dummy text of the printing and typesetting industry. Lorem Ipsum has been the industry's standard dummy text ever since the 1500s, when an unknown printer took a galley of type and scrambled it to make a type specimen book. It has survived not only five centuries, but also the leap into electronic typesetting, remaining essentially unchanged. It was popularised in the 1960s with the release of Lettrafold sheets containing Lorem Ipsum passages, and more recently with desktop publishing software like Paginor Studio including versions of Lorem Ipsum</p>
<a class="abs btn-orange about-btn">Learn More About Us</a>
<div class="abs about-hline"></div>

<!-- Services -->
<p class="abs center eyebrow svc-eyebrow">OUR CORE SERVICES</p>
<svg class="abs svc-orn" viewBox="0 0 80 12"><line x1="0" y1="6" x2="32" y2="6" stroke="#ccc"/><line x1="48" y1="6" x2="80" y2="6" stroke="#ccc"/><rect x="38" y="0" width="4" height="5" fill="#f5821f"/><rect x="38" y="7" width="4" height="5" fill="#5bbfc6"/><rect x="33" y="4" width="5" height="4" fill="#5bbfc6"/><rect x="42" y="4" width="5" height="4" fill="#f5821f"/></svg>
<h2 class="abs center svc-title">Transformative Services For Real Results</h2>

<article class="abs card" style="left:141px">
  <div class="img" role="img" aria-label="Therapist listening to a client in a one-on-one session" style="background:linear-gradient(135deg,#d9cfc6,#b9aba0 50%,#e8e2dc)"></div>
  <h3>Individual Therapy</h3>
  <p>Lorem Ipsum is simply dummy text of the printing and typesetting industry. Lorem Ipsum has been the.</p>
  <div class="badge"><svg width="24" height="24" viewBox="0 0 24 24" fill="none" stroke="#fff" stroke-width="1.5"><path d="M12 3 C7 3 4 6 4 10 C4 13 6 14 7 15 V21 H13 V18 H16 C18 18 19 16 19 14 L21 13 L19 10 C19 6 16 3 12 3Z"/><circle cx="12" cy="10" r="2.5"/></svg></div>
</article>
<article class="abs card" style="left:459px">
  <div class="img" role="img" aria-label="Group of medical staff in white coats standing together" style="background:linear-gradient(135deg,#c7ccd1,#8e969e 50%,#dde1e4)"></div>
  <h3>Support Groups</h3>
  <p>Lorem Ipsum is simply dummy text of the printing and typesetting industry. Lorem Ipsum has been the.</p>
  <div class="badge"><svg width="24" height="24" viewBox="0 0 24 24" fill="none" stroke="#fff" stroke-width="1.5"><circle cx="8" cy="7" r="3"/><circle cx="16" cy="7" r="3"/><path d="M2 20 C2 15 5 13 8 13 C11 13 14 15 14 20"/><path d="M14 13.5 C18 13 22 15 22 20"/></svg></div>
</article>
<article class="abs card" style="left:777px">
  <div class="img" role="img" aria-label="Nurse comforting an older patient in a clinic room" style="background:linear-gradient(135deg,#2d4f7a,#6d9cc4 50%,#c9dbe8)"></div>
  <h3>Counseling</h3>
  <p>Lorem Ipsum is simply dummy text of the printing and typesetting industry. Lorem Ipsum has been the.</p>
  <div class="badge"><svg width="24" height="24" viewBox="0 0 24 24" fill="none" stroke="#fff" stroke-width="1.5"><rect x="3" y="4" width="18" height="13" rx="2"/><path d="M8 17 L6 21 L12 17"/><path d="M7 9 H17 M7 12.5 H14"/></svg></div>
</article>

<!-- Ready -->
<section class="abs ready">
  <div class="ready-photo" role="img" aria-label="Doctor holding a clipboard while reassuring a smiling patient"></div>
  <h2>Ready To Begin<br>Your Journey To Wellness?</h2>
  <p>Get started on the path to health through the quality medical care our team provides!</p>
  <a class="btn-outline">Schedule Your Appointment</a>
</section>

<!-- Values strip -->
<div class="abs values"><span class="outline">Trustworthy_ </span><span class="solid">Caring</span><span class="outline">_ Professional</span></div>

<!-- Testimonials -->
<h2 class="abs center testi-title">What Our Clients Are Saying – Real Success Stories<br>from Trusted Partners</h2>

<article class="abs tcard" style="left:-158px">
  <div class="quote"><svg width="16" height="14" viewBox="0 0 16 14" fill="#5bbfc6"><path d="M1 7 C1 3 3 1 6 0.5 V3 C4.5 3.5 4 4.5 4 6 H6.5 V13 H1Z M9.5 7 C9.5 3 11.5 1 14.5 0.5 V3 C13 3.5 12.5 4.5 12.5 6 H15 V13 H9.5Z"/></svg></div>
  <div class="stars">★★★☆☆</div>
  <p>Lorem Ipsum is simply dummy text of the printing and typesetting industry. Lorem Ipsum has been the industry's standard dummy text ever since the 1500s, when an unknown printer took a galley of type.</p>
</article>
<article class="abs tcard o" style="left:151px">
  <div class="quote"><svg width="16" height="14" viewBox="0 0 16 14" fill="#f5821f"><path d="M1 7 C1 3 3 1 6 0.5 V3 C4.5 3.5 4 4.5 4 6 H6.5 V13 H1Z M9.5 7 C9.5 3 11.5 1 14.5 0.5 V3 C13 3.5 12.5 4.5 12.5 6 H15 V13 H9.5Z"/></svg></div>
  <div class="avatar" role="img" aria-label="Client portrait"></div>
  <div class="stars">★★★☆☆</div>
  <h4>Theo Marlin</h4>
  <p>Lorem Ipsum is simply dummy text of the printing and typesetting industry. Lorem Ipsum has been the industry's standard dummy text ever since the 1500s.</p>
</article>
<article class="abs tcard" style="left:459px">
  <div class="quote"><svg width="16" height="14" viewBox="0 0 16 14" fill="#5bbfc6"><path d="M1 7 C1 3 3 1 6 0.5 V3 C4.5 3.5 4 4.5 4 6 H6.5 V13 H1Z M9.5 7 C9.5 3 11.5 1 14.5 0.5 V3 C13 3.5 12.5 4.5 12.5 6 H15 V13 H9.5Z"/></svg></div>
  <div class="avatar" role="img" aria-label="Client portrait"></div>
  <div class="stars">★★★☆☆</div>
  <h4>Kiran Walbeck</h4>
  <p>Lorem Ipsum is simply dummy text of the printing and typesetting industry. Lorem Ipsum has been the industry's.</p>
</article>
<article class="abs tcard o" style="left:766px">
  <div class="quote"><svg width="16" height="14" viewBox="0 0 16 14" fill="#f5821f"><path d="M1 7 C1 3 3 1 6 0.5 V3 C4.5 3.5 4 4.5 4 6 H6.5 V13 H1Z M9.5 7 C9.5 3 11.5 1 14.5 0.5 V3 C13 3.5 12.5 4.5 12.5 6 H15 V13 H9.5Z"/></svg></div>
  <div class="avatar" role="img" aria-label="Client portrait"></div>
  <div class="stars">★★★☆☆</div>
  <h4>Dana Velloro</h4>
  <p>Lorem Ipsum is simply dummy text of the printing and typesetting industry. Lorem Ipsum has been the industry's standard dummy text ever since the 1500s, when an unknown printer took a galley of type.</p>
</article>
<article class="abs tcard" style="left:1073px">
  <div class="avatar" role="img" aria-label="Client portrait"></div>
  <div class="stars">★★★☆☆</div>
  <h4>Mira Oskalen</h4>
  <p>Lorem Ipsum is simply dummy text of the printing and typesetting industry. Lorem Ipsum has been the industry's standard dummy text ever.</p>
</article>
<div class="abs dots"><i class="on"></i><i></i><i></i><i></i><i></i></div>

<!-- Footer -->
<footer class="abs footer">
  <div class="abs f-logo"><span class="dot"></span>Nuvela Health</div>
  <p class="abs f-desc">Committed to providing expert mental health care in Washington DC, we empower individuals to heal, grow, and thrive</p>
  <div class="abs" style="left:368px;top:120px"><h4 class="f-head">Quick Links</h4></div>
  <ul class="abs f-links">
    <li>Home</li><li>About Us</li><li>Services</li><li>Blog</li><li>FAQs</li><li>Contact Us</li>
  </ul>
  <div class="abs f-contact" style="top:120px">
    <h4 class="f-head">Contact Info</h4>
    <p style="margin-top:18px">2217 Larkspur Avenue Suite 4, Brenmoor, Ohio 44902, United States</p>
    <p class="lbl">Email Address :</p>
    <p>info@NuvelaHealth.com</p>
    <p class="lbl">Phone Number :</p>
    <p>(555)-014-2290</p>
  </div>
  <div class="abs f-box">
    <h4 class="f-head">Stay in Touch</h4>
    <p>Stay updated with health tips and exclusive offers!</p>
    <div class="f-input">Email address
      <svg width="16" height="12" viewBox="0 0 16 12"><rect x="0.5" y="0.5" width="15" height="11" fill="#8a8f98"/><path d="M0.5 0.5 L8 7 L15.5 0.5" stroke="#fff" fill="none"/></svg></div>
    <div class="f-sub">Subscribe
      <svg width="14" height="14" viewBox="0 0 14 14"><path d="M1 1 L13 7 L1 13 L3 7Z" fill="#fff"/></svg></div>
  </div>
  <div class="abs f-rule"></div>
  <p class="abs f-copy">Copyright © 2025 Nuvela Mental Health | All Rights Reserved.</p>
  <p class="abs f-legal"><span>Terms &amp; Condition</span><span>|</span><span>Privacy Policy</span><span>|</span><span>Support</span></p>
</footer>

</body>
</html>
```